Logo + Label Design (Men’s Grooming Brand & Product Packaging)

Design a logo and 2 oz pomade label for Rook, a modern men’s grooming brand focused on clean, high-quality, natural ingredients. The design should establish a bold, masculine, minimalist identity that can later extend to products like shaving gel and body wash.

Key Requirements

Create a primary logo for “Rook” and a core label for the 2 oz pomade jar (screw-top).

Use a clean, modern style — masculine, confident, and approachable (think Milton’s, Velta, Northern Guild).

Design for 1–2 color screen printing on solid jar colors (white, black, or navy).

Avoid gradients, foil, or embossing. Must work in black & white.

Provide: vector logo, mockup of the 2 oz jar, color palette (CMYK/RGB/HEX), and font specs.

Winning design may lead to future projects (body wash, shave gel, skincare lines).

Font styles to use
Other font styles liked:
• We like the fonts and design concept in the attached mockup.

Requirements
Should not have
• We want to avoid too much writing or busy designs. We want to avoid having graphics/illustrations embedded in the logo if they will cause the brand to look less classy or sophisticated. We also want the design to look simple and all-American (e.g. Pemberton and Vale, Tall Pine, The LOFT, etc). We’d like to give a Halloway & Brinks vibe that feels classy and high end.

```html
<!DOCTYPE html>
<html lang="en">
<head>
<meta charset="utf-8">
<title>Rook Hair Pomade – Lid Label</title>
<link rel="stylesheet" href="https://fonts.googleapis.com/css2?family=Anton&family=Archivo+Black&family=Montserrat:wght@400;500;800&display=swap">
<style>
  :root {
    --backdrop: #434343;
    --lid: #3b3a38;
    --lid-edge: #353432;
    --ink-white: #f3f2ef;
    --ink-black: #000000;
    --accent-orange: #ee5a24;
  }
  html, body {
    margin: 0;
    padding: 0;
    width: 1200px;
    height: 644px;
    overflow: hidden;
    background: var(--backdrop);
  }
  .canvas {
    position: relative;
    width: 1200px;
    height: 644px;
  }
  .lid {
    position: absolute;
    left: 403px;
    top: 114px;
    width: 394px;
    height: 394px;
    border-radius: 50%;
    background: var(--lid);
    box-shadow: 0 0 0 1px var(--lid-edge);
  }
  .brand-badge {
    position: absolute;
    left: 564px;
    top: 131px;
    width: 72px;
    height: 72px;
    border-radius: 50%;
    background: var(--ink-black);
    display: flex;
    align-items: center;
    justify-content: center;
  }
  .brand-name {
    font-family: "Archivo Black", sans-serif;
    font-size: 19px;
    color: var(--ink-white);
    letter-spacing: 0.3px;
  }
  .product-title {
    position: absolute;
    left: 0;
    width: 1200px;
    text-align: center;
    font-family: "Anton", sans-serif;
    color: var(--ink-white);
    line-height: 1;
  }
  .product-title span {
    display: inline-block;
    transform: skewX(-8deg) scaleX(0.75);
  }
  .product-title--hair {
    top: 223px;
    font-size: 90px;
    letter-spacing: -2px;
  }
  .product-title--pomade {
    top: 296px;
    font-size: 86px;
    letter-spacing: -2px;
  }
  .net-weight {
    position: absolute;
    left: 0;
    width: 1200px;
    top: 377px;
    text-align: center;
    font-family: "Montserrat", sans-serif;
    font-weight: 500;
    font-size: 12.5px;
    color: var(--ink-white);
    letter-spacing: -0.3px;
  }
  .side-word {
    position: absolute;
    font-family: "Archivo Black", sans-serif;
    font-size: 27px;
    color: var(--ink-white);
    line-height: 1;
    white-space: nowrap;
  }
  .side-word--fresh {
    left: 431px;
    top: 314px;
    transform: translate(-50%, -50%) rotate(-82deg);
  }
  .side-word--clean {
    left: 763px;
    top: 310px;
    transform: translate(-50%, -50%) rotate(82deg);
  }
  .hold-arc {
    position: absolute;
    left: 0;
    top: 0;
  }
  .hold-arc__strength {
    font-family: "Montserrat", sans-serif;
    font-weight: 800;
    font-size: 19px;
    fill: var(--accent-orange);
  }
  .hold-arc__finish {
    font-family: "Montserrat", sans-serif;
    font-weight: 400;
    font-size: 18px;
    fill: var(--ink-white);
  }
</style>
</head>
<body>
  <main class="canvas">
    <div class="lid"></div>

    <div class="brand-badge"><span class="brand-name">ROOK</span></div>

    <div class="product-title product-title--hair"><span>Hair</span></div>
    <div class="product-title product-title--pomade"><span>Pomade</span></div>
    <div class="net-weight">NET WT 2 OZ (57 G)</div>

    <div class="side-word side-word--fresh">FRESH</div>
    <div class="side-word side-word--clean">CLEAN</div>

    <svg class="hold-arc" width="1200" height="644" viewBox="0 0 1200 644">
      <defs>
        <path id="arc-strength" d="M 469 331 A 131 131 0 0 0 731 331"/>
        <path id="arc-finish" d="M 473 355 A 127 127 0 0 0 727 355"/>
      </defs>
      <text class="hold-arc__strength">
        <textPath href="#arc-strength" startOffset="50%" text-anchor="middle" textLength="162" lengthAdjust="spacingAndGlyphs">MEDIUM HOLD</textPath>
      </text>
      <text class="hold-arc__finish">
        <textPath href="#arc-finish" startOffset="50%" text-anchor="middle" textLength="148" lengthAdjust="spacingAndGlyphs">MATTE FINISH</textPath>
      </text>
    </svg>
  </main>
</body>
</html>
```